Looking for a cutting-edge design for a healthy, all-nautural dog treats package

We are launching an All-Natural dog treat. It is made of 5 simple ingredients (peanut butter, sweet potatoes, potato flour, flaxseed oil & eggs). This product is white-labeled (meaning the original manufacturer will be producing them for us under our own name). The brand name is TrailHop.

What We Are Looking For:
We are looking for an approach that really emphasizes the fact that it will be all-natural, grain-free. In fact, we are looking for a design that is very similar to the qu loaf (please take a look at quloafdemo.net for examples).

Other Details to Remember:
Attached is a png file of the dimensions provided by the original manufacturer. Please note that our bag will the a "brown paper bag" color. Finally, the back of the bag should include the same verbiage as the original (although does not have to be the same design/fonts).
Updates

Project Deadline Extended Reason: It appears that the package can now only be in one color on "brown paper bag" of "off white" packaging. Added Wednesday, October 26, 2016

Target Market(s)

Dog owners that appreciate quality food for their pets...more than likely, they are foodies themselves and/or health conscience

Industry/Entity Type

Pet

Logo Text

TrailHop

Requirements
Must have
• Emphasis on the product being all-natural, grain-free. Looks similar to the quloaf packaging (quloafdemo.net)
• **IMPORTANT UPDATE**
• The packaging people have notified us that all graphics or lettering must be in ONE SAME COLOR. The package itself will be in either "brown paper bag" or "off white" color.
Should not have
• That being said, please do NOT make it look absolutely identical to the qu loaf

```html
<!DOCTYPE html>
<html lang="en">
<head>
<meta charset="utf-8">
<title>TrailHop Dog Treat Pouch</title>
<link href="https://fonts.googleapis.com/css2?family=Oswald:wght@300;600&family=Special+Elite&display=swap" rel="stylesheet">
<style>
  :root {
    --backdrop: #f6f1e2;
    --kraft: #c8a27a;
    --kraft-dark: #b88f66;
    --label-red: #d8231f;
    --cream: #f4e4c9;
    --treat-light: #d9ab6e;
    --treat-dark: #a9743f;
  }
  * { margin: 0; padding: 0; box-sizing: border-box; }
  html, body {
    width: 1156px;
    height: 1200px;
    overflow: hidden;
    background: var(--backdrop);
  }
  .pouch {
    position: absolute;
    left: 198px;
    top: 60px;
    width: 760px;
    height: 1080px;
    background: linear-gradient(180deg, var(--kraft) 0%, var(--kraft-dark) 100%);
    border-radius: 6px;
  }
  .pouch__seal {
    position: absolute;
    left: 0; right: 0; top: 26px;
    height: 2px;
    background: rgba(0,0,0,0.08);
  }
  .label {
    position: absolute;
    left: 0;
    top: 55px;
    width: 760px;
    height: 610px;
    background: var(--label-red);
    color: var(--cream);
  }
  .label__title {
    position: absolute;
    left: 38px;
    top: 26px;
    font-family: "Oswald", sans-serif;
    font-weight: 600;
    font-size: 90px;
    line-height: 1;
    letter-spacing: 0.5px;
  }
  .label__divider {
    position: absolute;
    left: 413px;
    top: 38px;
    width: 2px;
    height: 160px;
    background: var(--cream);
  }
  .label__claim {
    position: absolute;
    left: 460px;
    top: 112px;
    font-family: "Special Elite", monospace;
    font-size: 34px;
  }
  .label__band {
    position: absolute;
    left: 34px;
    top: 226px;
    width: 663px;
    height: 46px;
    background: var(--cream);
    color: var(--label-red);
    font-family: "Oswald", sans-serif;
    font-weight: 600;
    font-size: 24px;
    line-height: 46px;
    padding-left: 50px;
  }
  .brand {
    position: absolute;
    left: 60px;
    top: 300px;
    display: flex;
    align-items: center;
    gap: 26px;
  }
  .brand__dot {
    width: 110px;
    height: 110px;
    border: 3px solid var(--cream);
    border-radius: 50%;
  }
  .brand__name {
    font-family: "Oswald", sans-serif;
    font-weight: 300;
    font-size: 64px;
    line-height: 0.98;
    letter-spacing: 1px;
  }
  .label__diet {
    position: absolute;
    left: 66px;
    top: 506px;
    width: 320px;
    border-top: 2px solid var(--cream);
    padding-top: 12px;
    font-family: "Special Elite", monospace;
    font-size: 24px;
    letter-spacing: 7px;
    line-height: 1.45;
  }
  .ingredients {
    position: absolute;
    left: 450px;
    top: 296px;
    width: 245px;
    list-style: none;
    font-family: "Special Elite", monospace;
    font-size: 25px;
  }
  .ingredients li {
    height: 53px;
    padding-top: 8px;
    border-bottom: 2px solid var(--cream);
  }
  .ingredients li:last-child { border-bottom: none; }
  .window {
    position: absolute;
    left: 20px;
    top: 670px;
    width: 720px;
    height: 300px;
    border-radius: 4px;
    background: radial-gradient(ellipse at 45% 45%, var(--treat-light) 0%, var(--treat-dark) 100%);
  }
</style>
</head>
<body>
  <main class="pouch">
    <div class="pouch__seal"></div>
    <section class="label">
      <h1 class="label__title">DOG TREAT</h1>
      <div class="label__divider"></div>
      <p class="label__claim">all-natural</p>
      <p class="label__band">SIMPLY MADE</p>
      <div class="brand">
        <span class="brand__dot"></span>
        <span class="brand__name">TRAIL<br>HOP</span>
      </div>
      <p class="label__diet">GRAIN-FREE<br>GLUTEN-FREE</p>
      <ul class="ingredients">
        <li>peanut butter</li>
        <li>sweet potatoes</li>
        <li>potato flour</li>
        <li>flaxseed</li>
        <li>oil &amp; eggs</li>
      </ul>
    </section>
    <div class="window" role="img" aria-label="Clear window showing bone-shaped baked dog treats"></div>
  </main>
</body>
</html>
```